Dr Tasneer's Letterhead

I need a professional neat letterhead incorporating my professional information, university titles and qualifications. I have attached my 3 recent ones which contain all the necessary information that needs to be included. I am happy for the information to be a side bar left or right, or as a header/footer combination.

Hello all

I have now made a 2nd and 3rd prize so please submit

Reason: Now there is a 2nd and 3rd place so I can take 3 designs

Industry/Entity Type

University

```html
<!DOCTYPE html>
<html lang="en">
<head>
<meta charset="utf-8">
<title>Dr Tasneer Letterhead</title>
<link href="https://fonts.googleapis.com/css2?family=Noto+Serif:wght@300;400;700&display=swap" rel="stylesheet">
<style>
  :root {
    --backdrop: #5a3f2c;
    --paper: #ffffff;
    --band: #b8b9bc;
    --ink: #2b2b2b;
    --ink-soft: #3d3d3d;
    --rule: #1a1a1a;
    --rule-soft: #8d8d8d;
    --badge-a: #2f3f7a;
    --badge-b: #d8a23a;
    --badge-c: #8a8a8a;
  }
  * { margin: 0; padding: 0; box-sizing: border-box; }
  html, body { width: 965px; height: 1200px; overflow: hidden; }
  body {
    background: var(--backdrop);
    position: relative;
    font-family: "Noto Serif", serif;
    color: var(--ink);
  }
  .letterhead {
    position: absolute;
    left: 72px; top: 73px;
    width: 820px; height: 1062px;
    background: var(--paper);
  }
  .header-band {
    position: absolute; left: 0; top: 0;
    width: 820px; height: 124px;
    background: var(--band);
  }
  .header-rule {
    position: absolute; left: 0; top: 125px;
    width: 820px; height: 3px;
    background: var(--rule);
  }
  .doctor-name {
    position: absolute; left: 24px; top: 17px;
    font-size: 26px; font-weight: 700; letter-spacing: -0.2px;
    color: var(--ink);
  }
  .doctor-credentials {
    position: absolute; left: 24px; top: 48px;
    font-size: 15px; font-weight: 300; letter-spacing: 1.1px;
    color: var(--ink-soft);
  }
  .contact-line {
    position: absolute; left: 24px; top: 92px;
    display: flex; align-items: center; gap: 8px;
    font-size: 15px; font-weight: 300; letter-spacing: 0.6px;
    color: var(--ink-soft);
  }
  .contact-item { display: flex; align-items: center; gap: 5px; margin-right: 4px; }
  .contact-item svg { width: 18px; height: 18px; }
  .appointments {
    position: absolute; right: 21px; top: 17px;
    text-align: right;
    font-size: 14.5px; font-weight: 300; line-height: 16px; letter-spacing: 0.7px;
    color: var(--ink-soft);
  }
  .footer-rule {
    position: absolute; left: 20px; top: 954px;
    width: 768px; height: 1px;
    background: var(--rule-soft);
  }
  .locations {
    position: absolute; left: 22px; top: 962px;
    font-size: 15px; font-weight: 300; line-height: 17px; letter-spacing: 0.7px;
    color: var(--ink-soft);
  }
  .location { position: relative; padding-left: 13px; margin-bottom: 4px; }
  .location svg { position: absolute; left: 0; top: 3px; width: 9px; height: 13px; }
  .affiliations {
    position: absolute; left: 469px; top: 966px;
    display: flex; align-items: center; gap: 20px;
  }
  .badge { display: block; }
  .college-mark {
    display: flex; align-items: center; gap: 8px;
    font-size: 16px; font-weight: 400; color: var(--ink-soft);
    margin-left: -14px;
  }
  .college-mark .mark-square { width: 30px; height: 30px; background: var(--badge-c); }
  .provider-numbers {
    position: absolute; left: 460px; top: 1029px;
    font-size: 16px; font-weight: 300; letter-spacing: 0.6px;
    color: var(--ink-soft);
  }
</style>
</head>
<body>
  <main class="letterhead">
    <header class="header-band">
      <h1 class="doctor-name">DR. SAMIR TASNEER</h1>
      <p class="doctor-credentials">BSc Med, MBBS (Hons 1) NCU</p>
      <div class="contact-line">
        <span class="contact-item">
          <svg viewBox="0 0 18 18"><circle cx="9" cy="9" r="8" fill="none" stroke="#333" stroke-width="1.3"/><path d="M6 4.5c-1 1-1 3 .5 5.5s3.5 4 5 3.8l.8-1.3-1.8-1.2-.9.8c-.8-.4-2-1.8-2.4-2.8l.8-.9-1-1.9z" fill="#333"/></svg>
          95550142
        </span>
        <span class="contact-item">
          <svg viewBox="0 0 18 18"><circle cx="9" cy="9" r="8" fill="none" stroke="#333" stroke-width="1.3"/><path d="M6 4.5c-1 1-1 3 .5 5.5s3.5 4 5 3.8l.8-1.3-1.8-1.2-.9.8c-.8-.4-2-1.8-2.4-2.8l.8-.9-1-1.9z" fill="#333"/></svg>
          95550387
        </span>
        <span class="contact-item">
          <svg viewBox="0 0 22 18" style="width:22px"><rect x="5" y="2" width="12" height="5" fill="#333"/><rect x="1" y="7" width="20" height="9" rx="2" fill="#333"/><rect x="6" y="10" width="10" height="2" fill="#b8b9bc"/></svg>
          95550619
        </span>
      </div>
      <div class="appointments">
        <p>Consultant ENT/Head and Neck Surgeon</p>
        <p>Harbourview Cancer Centre</p>
        <p>Eastfield Hospital</p>
        <p>Northern Coast Health District (NCHD)</p>
        <p>Senior Lecturer, University of Redfield (URed)</p>
        <p>&amp; Coastal Plains (UCP)</p>
      </div>
    </header>
    <div class="header-rule"></div>

    <footer>
      <div class="footer-rule"></div>
      <div class="locations">
        <div class="location">
          <svg viewBox="0 0 9 13"><path d="M4.5 0a4.3 4.3 0 0 0-4.3 4.3C.2 7.5 4.5 13 4.5 13s4.3-5.5 4.3-8.7A4.3 4.3 0 0 0 4.5 0zm0 6.2a1.9 1.9 0 1 1 0-3.8 1.9 1.9 0 0 1 0 3.8z" fill="#333"/></svg>
          Parkside Medical Centre<br>104/151 Linden Rd., Eastfield NSW 2199
        </div>
        <div class="location">
          <svg viewBox="0 0 9 13"><path d="M4.5 0a4.3 4.3 0 0 0-4.3 4.3C.2 7.5 4.5 13 4.5 13s4.3-5.5 4.3-8.7A4.3 4.3 0 0 0 4.5 0zm0 6.2a1.9 1.9 0 1 1 0-3.8 1.9 1.9 0 0 1 0 3.8z" fill="#333"/></svg>
          Ashgrove Specialist Centre<br>11 Ashgrove Highway, Millbrook NSW 2198
        </div>
        <div class="location">
          <svg viewBox="0 0 9 13"><path d="M4.5 0a4.3 4.3 0 0 0-4.3 4.3C.2 7.5 4.5 13 4.5 13s4.3-5.5 4.3-8.7A4.3 4.3 0 0 0 4.5 0zm0 6.2a1.9 1.9 0 1 1 0-3.8 1.9 1.9 0 0 1 0 3.8z" fill="#333"/></svg>
          27 Kestrel Street Havenwood 2797
        </div>
      </div>

      <div class="affiliations">
        <svg class="badge" width="50" height="58" viewBox="0 0 50 58" role="img" aria-label="University affiliation badge">
          <path d="M1 1h48v30c0 14-12 24-24 26C13 55 1 45 1 31z" fill="var(--badge-a)"/>
        </svg>
        <svg class="badge" width="66" height="60" viewBox="0 0 66 60" role="img" aria-label="University affiliation badge">
          <path d="M10 4h46v28c0 14-11 24-23 26C21 56 10 46 10 32z" fill="var(--badge-b)"/>
        </svg>
        <div class="college-mark">
          <span class="mark-square" role="img" aria-label="Surgical college badge"></span>
          <span>Coastal Surgeons</span>
        </div>
      </div>
      <p class="provider-numbers">Provider 4500871A, 240613KX, 240613KY</p>
    </footer>
  </main>
</body>
</html>
```